Restaurant Finder Website Design

I need to create a website that will help people find restaurants around a zip code or address.

I would like to have a very clean and simple design. I will need a design for the homepage, that should be very clean and simple to use. its where the users will launch their search. I am thinking something like tavlex like.. big search field with a very clean page where users can create an account or restaurants subscribe to the service.

Also need the design of the search results page, I would like to display a big map with the results and a list on the side or the bottom of the map.

Also need a profile page for the users that sign up to the site.

Mostly what I need are guidelines and color coordinated elements, like a general layout and buttons that work together. I would like to know what the action buttons and elements should look like. Because its going to have some more detail pages.

Target Market(s)

People in general, mainly people that work at an office and have to find a place for lunch every day.

Industry/Entity Type

Restaurant

Number of Pages Required

4 page

Font styles to use
Serif
Sans Serif

Requirements
Must have
• It must be a really simple and clean design but look edgy.

```html
<!DOCTYPE html>
<html lang="en">
<head>
<meta charset="utf-8">
<title>Munchway – Find restaurants near you</title>
<link href="https://fonts.googleapis.com/css2?family=Open+Sans:wght@400;600&display=swap" rel="stylesheet">
<style>
  :root {
    --brand-red: #c9202a;
    --link-red: #e0242e;
    --white: #ffffff;
    --field-text: #666666;
    --field-icon: #8a8a8a;
    --divider: #d6d6d6;
    --header-bg: rgba(0, 0, 0, 0.78);
    --panel-bg: rgba(0, 0, 0, 0.62);
    --tagline: #d0d0d0;
  }
  * { margin: 0; padding: 0; box-sizing: border-box; }
  html, body { width: 1200px; height: 709px; overflow: hidden; }
  body { font-family: "Open Sans", Arial, sans-serif; position: relative; background: #1a1a1a; }

  .hero-photo {
    position: absolute; inset: 0;
    background:
      radial-gradient(ellipse at 45% 40%, rgba(200,190,185,0.55), transparent 55%),
      radial-gradient(ellipse at 90% 35%, rgba(235,230,225,0.45), transparent 40%),
      linear-gradient(180deg, #6f6a6c 0%, #7b7578 35%, #3a3436 70%, #1c1819 100%);
  }
  .hero-shade { position: absolute; inset: 0; background: rgba(0,0,0,0.35); }

  .site-header {
    position: absolute; top: 0; left: 0; width: 1200px; height: 114px;
    background: var(--header-bg);
  }
  .brand {
    position: absolute; left: 60px; top: 19px; height: 76px;
    display: flex; align-items: center; gap: 12px;
  }
  .brand-dot { width: 70px; height: 70px; border-radius: 50%; background: var(--brand-red); }
  .brand-name { color: var(--white); font-size: 35px; font-weight: 400; letter-spacing: -0.5px; }

  .account-links {
    position: absolute; right: 60px; top: 46px;
    font-size: 12px; color: var(--link-red);
  }
  .account-links a { color: var(--link-red); text-decoration: none; }
  .account-links .sep { margin: 0 9px; }

  .search-panel {
    position: absolute; left: 61px; top: 375px; width: 1079px; height: 269px;
    background: var(--panel-bg);
  }
  .search-form { position: absolute; left: 82px; top: 45px; display: flex; height: 62px; }
  .field {
    width: 354px; height: 62px; background: var(--white);
    display: flex; align-items: center; padding-left: 16px; gap: 8px;
    font-size: 12px; color: var(--field-text);
  }
  .field + .field { border-left: 1px solid var(--divider); width: 353px; }
  .field svg { flex: none; }
  .search-button {
    width: 209px; height: 62px; background: var(--brand-red); color: var(--white);
    border: none; font-family: inherit; font-size: 20px; font-weight: 600;
    display: flex; align-items: center; justify-content: center;
  }
  .alt-options {
    position: absolute; left: 0; right: 0; top: 127px; text-align: center;
    color: var(--white); font-size: 13px;
  }
  .alt-links { display: flex; justify-content: center; gap: 26px; margin-top: 11px; }
  .alt-link { display: flex; align-items: center; gap: 10px; color: var(--white); text-decoration: none; font-size: 13px; }
  .alt-dot { width: 20px; height: 20px; border-radius: 50%; background: var(--brand-red); }
  .tagline {
    position: absolute; left: 0; right: 0; top: 225px; text-align: center;
    color: var(--tagline); font-size: 16px;
  }
</style>
</head>
<body>
  <div class="hero-photo" role="img" aria-label="Photo of a smiling diner ordering from a waitress in a bright restaurant"></div>
  <div class="hero-shade"></div>

  <header class="site-header">
    <div class="brand">
      <span class="brand-dot"></span>
      <span class="brand-name">Munchway</span>
    </div>
    <nav class="account-links">
      <a href="#">Log In</a><span class="sep">|</span><a href="#">Sing Up</a>
    </nav>
  </header>

  <section class="search-panel">
    <form class="search-form">
      <label class="field">
        <svg width="22" height="30" viewBox="0 0 22 30"><path d="M11 1.5C5.8 1.5 1.8 5.5 1.8 10.6 1.8 17 11 28 11 28s9.2-11 9.2-17.4C20.2 5.5 16.2 1.5 11 1.5z" fill="none" stroke="var(--field-icon)" stroke-width="1.8"/><circle cx="11" cy="10.5" r="3.6" fill="none" stroke="var(--field-icon)" stroke-width="1.8"/></svg>
        Select City
      </label>
      <label class="field">
        <svg width="18" height="26" viewBox="0 0 18 26"><rect x="2" y="1" width="14" height="24" fill="var(--field-icon)"/><g fill="var(--white)"><rect x="5" y="4" width="3" height="3"/><rect x="10" y="4" width="3" height="3"/><rect x="5" y="10" width="3" height="3"/><rect x="10" y="10" width="3" height="3"/><rect x="5" y="16" width="3" height="3"/><rect x="10" y="16" width="3" height="3"/><rect x="7.5" y="21" width="3" height="4"/></g></svg>
        zip code
      </label>
      <button type="button" class="search-button">SEARCH</button>
    </form>

    <div class="alt-options">
      <div>OR</div>
      <div class="alt-links">
        <a href="#" class="alt-link"><span class="alt-dot"></span>USE PLOTTA MAP</a>
        <a href="#" class="alt-link"><span class="alt-dot"></span>I HAVE A PLOTTA</a>
      </div>
    </div>

    <p class="tagline">30 Million Foodies use Munchway Every Month</p>
  </section>
</body>
</html>
```